Business Card Design & Logo Design

Im a new company selling: balloons, bespoke gift wrapping services & Christmas decorating services i.e. I will come and decorate your tree, wrap your xmas presents, set & decorate your dining table, help you host your xmas party etc. etc.

I don't do 'cheesey' stuff so need a sophisticated card.

I love b&w colours, I love stripes and smart looking stuff.

I do already have an idea and if I don't find anything else then I will go with my idea but would then just need somebody to create the artwork for me.

www.copperwillow.co.uk is currently in the process of being designed so any ideas of logos/designs must also work with a website.

Industry/Entity Type

Business

Contact Information for Business Card

Copper Willow
Elmsbrook upon Tarn
KT14 9RD
Thornleyshire
01632 960418
or
07700 900736

treats@copperwillow.co.uk

```html
<!DOCTYPE html>
<html lang="en">
<head>
<meta charset="utf-8">
<title>Copper Willow Elmsbrook – Business Card</title>
<link rel="stylesheet" href="https://fonts.googleapis.com/css2?family=Open+Sans:wght@300&family=Roboto:wght@300&display=swap">
<style>
  :root {
    --ink-dark: #20282a;
    --slate-mid: #56666a;
    --slate-glow: #5a6a6a;
    --ink-black: #0b0d0d;
    --stripe-white: #ffffff;
    --title-blue: #4cb9eb;
    --dot-green: #3f9a48;
    --dot-green-light: #46a24e;
    --dot-violet: #a046b8;
    --dot-violet-deep: #9440a8;
    --dot-teal: #4a9cc2;
    --dot-teal-deep: #3f8aab;
    --contact-white: #ffffff;
  }
  * { margin: 0; padding: 0; box-sizing: border-box; }
  html, body {
    width: 1200px;
    height: 791px;
    overflow: hidden;
    background: var(--ink-black);
  }
  .business-card {
    position: relative;
    width: 1200px;
    height: 791px;
    overflow: hidden;
    background: linear-gradient(112deg,
      var(--ink-dark) 0%,
      #3a4649 22%,
      var(--slate-mid) 45%,
      var(--slate-glow) 52%,
      #3d4848 66%,
      #1a1f1f 82%,
      var(--ink-black) 100%);
  }
  .stripe {
    position: absolute;
    top: 51px;
    width: 60px;
    height: 689px;
    background: var(--stripe-white);
  }
  .stripe--one { left: 53px; }
  .stripe--two { left: 137px; }
  .stripe--three { left: 225px; }
  .dots {
    position: absolute;
    inset: 0;
    width: 1200px;
    height: 791px;
  }
  .brand-title {
    position: absolute;
    left: 322px;
    top: 343px;
    font-family: "Open Sans", "Segoe UI", sans-serif;
    font-weight: 300;
    font-size: 104px;
    line-height: 1;
    letter-spacing: -3px;
    color: var(--title-blue);
    white-space: nowrap;
    transform: scaleX(0.76);
    transform-origin: left top;
  }
  .contact {
    position: absolute;
    right: 53px;
    top: 564px;
    font-family: "Roboto", "Helvetica Neue", sans-serif;
    font-weight: 300;
    font-size: 24.5px;
    line-height: 34.5px;
    color: var(--contact-white);
    text-align: right;
    font-style: normal;
    letter-spacing: 0;
  }
  .contact p { white-space: nowrap; }
  .contact .contact-email { margin-right: -8px; }
</style>
</head>
<body>
  <main class="business-card">
    <div class="stripe stripe--one"></div>
    <div class="stripe stripe--two"></div>
    <div class="stripe stripe--three"></div>

    <svg class="dots" viewBox="0 0 1200 791" aria-hidden="true">
      <defs>
        <linearGradient id="green-fill" x1="0" y1="0" x2="1" y2="1">
          <stop offset="0" stop-color="var(--dot-green)"/>
          <stop offset="1" stop-color="var(--dot-green-light)"/>
        </linearGradient>
        <linearGradient id="violet-fill" x1="0" y1="0" x2="1" y2="1">
          <stop offset="0" stop-color="var(--dot-violet)"/>
          <stop offset="1" stop-color="var(--dot-violet-deep)"/>
        </linearGradient>
        <linearGradient id="teal-fill" x1="0" y1="0" x2="1" y2="1">
          <stop offset="0" stop-color="var(--dot-teal)"/>
          <stop offset="1" stop-color="var(--dot-teal-deep)"/>
        </linearGradient>
      </defs>
      <circle class="dot dot--green" cx="416" cy="210" r="96" fill="url(#green-fill)"/>
      <ellipse class="dot dot--violet-small" cx="864" cy="209" rx="79" ry="73" fill="url(#violet-fill)"/>
      <circle class="dot dot--violet-large" cx="445" cy="560" r="96" fill="url(#violet-fill)"/>
      <ellipse class="dot dot--teal" cx="696" cy="594" rx="67" ry="64" fill="url(#teal-fill)"/>
    </svg>

    <h1 class="brand-title">Copper Willow Elmsbrook</h1>

    <address class="contact">
      <p>Copper Willow Elmsbrook upon</p>
      <p>Tarn KT14 9RD Thornleyshire</p>
      <p>01632 960418 or 07700 900736</p>
      <p class="contact-email">treats@copperwillow.co.uk</p>
    </address>
  </main>
</body>
</html>
```